Business Consultants - Require an A4 size presentation folder with inserts for a new exciting Standa

We have developed a service/product where we help small and medium businesses to draft up their policies & procedures manual for their business. This manual has everything in it on how to run their business. From how to answer the phone, to how to process invoices, through to HR information, and marketing plans.

We need a professional but modern looking presentation folder to house all this information. The size will be A4. Inside we will have up to 12 inserts to seperate the different chapters/topic. For example. Sales, Marketing, Administration, Operations, Finance.

Each folder will be branded with the client logo and name on the front, hence it does need to be relativity simple and neutral as to not clash with their colours etc.

We will have our Logo and contact details on the back of the folder.

The design aspect may well come for the chapter inserts. Again the actual tabs will need to be neutral so that we can write on them so that when you open the front cover you can quickly go the chapter you need.

Be warned I do not want any generic design gallery type designs. They stand out as cheap and nasty. I need you actually put some thought into these !!!

Attached is our Logo, and a two photos of the sort of shape and size of the anticipated folders.
Updates

Target Market(s)

Small & Medium Brick & Mortar Business Owners

Industry/Entity Type

Business Consultant

Colors

Designer to choose colors to be used in the design.

Requirements
Must have
• Must be clean, crisp, but with some cool simple design elements
Should not have
• Too many bold colours as it will clash with our client logos, which we have no control over what colour they are

```html
<!DOCTYPE html>
<html lang="en">
<head>
<meta charset="utf-8">
<title>Chapter Insert – IT</title>
<link rel="stylesheet" href="https://fonts.googleapis.com/css2?family=Open+Sans:wght@700;800&display=swap">
<style>
  :root {
    --backdrop: #eeeeec;
    --paper: #ffffff;
    --ink: #0a0a0a;
    --accent: #f1b41c;
    --tab: #566b2e;
    --tab-text: #e7ecd9;
    --text-light: #ffffff;
    --photo-sky: #a9bfd3;
    --photo-mid: #6f7f8e;
    --photo-city: #4a4336;
  }
  * { box-sizing: border-box; margin: 0; padding: 0; }
  html, body {
    width: 1200px;
    height: 800px;
    overflow: hidden;
    background: var(--backdrop);
    font-family: "Open Sans", Arial, sans-serif;
  }
  .canvas {
    position: relative;
    width: 1200px;
    height: 800px;
  }
  .insert {
    position: absolute;
    left: 340px;
    top: 50px;
    width: 520px;
    height: 700px;
    background: var(--paper);
    box-shadow: 0 2px 10px rgba(0,0,0,0.12);
  }
  .insert__photo {
    position: absolute;
    left: 0;
    top: 0;
    width: 490px;
    height: 365px;
    background: linear-gradient(180deg, var(--photo-sky) 0%, var(--photo-mid) 55%, var(--photo-city) 100%);
  }
  .insert__shapes {
    position: absolute;
    left: 0;
    top: 0;
    width: 520px;
    height: 700px;
  }
  .insert__content {
    position: absolute;
    left: 36px;
    top: 445px;
    color: var(--text-light);
  }
  .chapter-title {
    font-size: 40px;
    font-weight: 800;
    line-height: 1;
    margin-bottom: 30px;
  }
  .chapter-intro {
    font-size: 11.5px;
    font-weight: 700;
    line-height: 14.5px;
    width: 240px;
  }
  .divider-tab {
    position: absolute;
    left: 860px;
    top: 470px;
    width: 26px;
    height: 78px;
    background: var(--tab);
    border-radius: 0 4px 4px 0;
    display: flex;
    align-items: center;
    justify-content: center;
  }
  .divider-tab__label {
    transform: rotate(90deg);
    color: var(--tab-text);
    font-size: 9px;
    font-weight: 700;
    letter-spacing: 1px;
  }
</style>
</head>
<body>
<div class="canvas">
  <div class="insert">
    <div class="insert__photo" role="img" aria-label="Businessman touching a virtual screen of sketched business diagrams over a city skyline at dusk"></div>
    <svg class="insert__shapes" viewBox="0 0 520 700" aria-hidden="true">
      <polygon points="0,357 254,357 520,628 520,700 0,700" fill="var(--accent)"/>
      <polygon points="0,365 246,365 520,644 520,700 0,700" fill="var(--ink)"/>
    </svg>
    <div class="insert__content">
      <h1 class="chapter-title">IT</h1>
      <p class="chapter-intro">
        Lorem ipsumLorem ipsumLorem ipsum<br>
        Lorem ipsumLorem ipsumLorem ipsum<br>
        Lorem ipsumLorem ipsumLorem ipsum<br>
        Lorem ipsumLorem ipsumLorem ipsum<br>
        Lorem ipsumLorem ipsumLorem ipsum<br>
        Lorem ipsumLorem ipsumLorem ipsum<br>
        Lorem ipsumLorem ipsum
      </p>
    </div>
  </div>
  <div class="divider-tab"><span class="divider-tab__label">IT</span></div>
</div>
</body>
</html>
```